Sunglasses from $19 - 900 something for everyone

Sunglasses from $19
We sell sunglasses from $19 - 900.
some of our brands include Kelo Vorn, Dex pold, Varne, Lex Brandt, Pimsett.
This poster will be in a store window that has lots of foot traffic My store colors are blue and orange.
I want to emphasize Starting price is $19.
If you can include a couple of the logos from the brands mentioned that would be helpful.
My store is in a historic tourist area of Downtown Annapolis.
We are located in a boating community with tourist from all over the world.
A pair of sunglasses and flip should be included on the poster.
The poster is to generate traffic into my store.

Target Market(s)

everyone

Industry/Entity Type

Sunglass Retail store

Font styles to use
Other font styles liked:
• Ariel, Sans Serif

Colors
0054AA
0677BA
7BADD7
CADEEF
E8F1F8
FFF300
FFF600
FEFA6F
FFFEC7
FFFEE8
FFC000
F8CF3A
FAE287
FDF2CF
FEFAEE
EE7325
F08F49
F5BC92
FAE3D3
FDF4ED

Requirements
Must have
• Color, Blue and orange and sunglasses
Nice to have
• logos of brands
Should not have
• cartoon feel, juvenile, inexpensive

```html
<!DOCTYPE html>
<html lang="en">
<head>
<meta charset="utf-8">
<title>Harbor Lens – Sunglasses from $19</title>
<link rel="stylesheet" href="https://fonts.googleapis.com/css2?family=Bebas+Neue&family=Gochi+Hand&family=Libre+Baskerville:wght@400&display=swap">
<style>
  :root {
    --backdrop: #22bfcd;
    --paper: #f2f2f2;
    --ink: #2b2229;
    --orange-deep: #ee7325;
    --orange-panel: #eb962a;
    --white: #ffffff;
    --teal-lens: #1fa6a6;
    --teal-dark: #0f3f4a;
    --frame: #1b1f3a;
    --sun-yellow: #f8cf3a;
  }
  html, body {
    margin: 0;
    padding: 0;
    width: 1200px;
    height: 900px;
    overflow: hidden;
    background: var(--backdrop);
  }
  .poster {
    position: absolute;
    left: 299px;
    top: 20px;
    width: 602px;
    height: 860px;
    background: var(--paper);
    overflow: hidden;
  }
  .headline {
    position: absolute;
    left: 43px;
    top: 763px;
    width: 630px;
    height: 112px;
    transform-origin: 0 0;
    transform: rotate(-90deg);
    margin: 0;
    font-family: "Bebas Neue", sans-serif;
    font-weight: 400;
    font-size: 160px;
    line-height: 112px;
    letter-spacing: 1px;
    color: var(--ink);
    white-space: nowrap;
  }
  .store-name {
    position: absolute;
    left: 223px;
    top: 52px;
    width: 320px;
    margin: 0;
    font-family: "Libre Baskerville", serif;
    font-weight: 400;
    font-size: 34px;
    letter-spacing: 2px;
    color: var(--orange-deep);
    text-align: center;
    white-space: nowrap;
  }
  .offer-panel {
    position: absolute;
    left: 191px;
    top: 135px;
    width: 359px;
    height: 623px;
    background: var(--orange-panel);
  }
  .offer-lead {
    position: absolute;
    left: 22px;
    top: 20px;
    margin: 0;
    font-family: "Gochi Hand", cursive;
    font-size: 32px;
    line-height: 30px;
    color: var(--white);
  }
  .offer-price {
    position: absolute;
    left: 18px;
    top: 118px;
    margin: 0;
    font-family: "Bebas Neue", sans-serif;
    font-size: 168px;
    line-height: 150px;
    color: var(--white);
  }
  .art {
    position: absolute;
    display: block;
  }
  .art-sunglasses {
    left: 170px;
    top: 322px;
    width: 422px;
    height: 390px;
    overflow: visible;
  }
  .art-flipflops {
    left: 229px;
    top: 454px;
    width: 101px;
    height: 140px;
    border-radius: 40px;
    background: linear-gradient(160deg, var(--sun-yellow), #f3a23a);
  }
  .art-mini-glasses {
    left: 85px;
    top: 280px;
    width: 58px;
    height: 40px;
    border-radius: 20px;
    background: linear-gradient(90deg, var(--sun-yellow), var(--backdrop));
  }
  .art-starfish-top {
    left: 43px;
    top: 42px;
    width: 54px;
    height: 53px;
    border-radius: 50%;
    background: var(--orange-deep);
  }
  .art-glasses-top {
    left: 92px;
    top: 26px;
    width: 60px;
    height: 104px;
    border-radius: 28px;
    background: linear-gradient(180deg, var(--backdrop), var(--sun-yellow));
  }
  .art-starfish-bottom {
    left: 88px;
    top: 758px;
    width: 53px;
    height: 51px;
    border-radius: 50%;
    background: var(--sun-yellow);
  }
  .brand-row {
    position: absolute;
    left: 213px;
    top: 784px;
    width: 330px;
    display: flex;
    justify-content: space-between;
    align-items: center;
    margin: 0;
    padding: 0;
    list-style: none;
  }
  .brand-name {
    font-family: "Libre Baskerville", serif;
    font-size: 19px;
    font-weight: 400;
    color: var(--ink);
    white-space: nowrap;
  }
</style>
</head>
<body>
  <main class="poster">
    <span class="art art-starfish-top" role="img" aria-label="Orange starfish illustration"></span>
    <span class="art art-glasses-top" role="img" aria-label="Small illustrated sunglasses with blue and yellow lenses"></span>
    <span class="art art-starfish-bottom" role="img" aria-label="Yellow starfish illustration"></span>

    <h1 class="headline">Sunglasses</h1>

    <p class="store-name">Harbor Lens</p>

    <section class="offer-panel">
      <p class="offer-lead">for<br>everyone<br>from</p>
      <p class="offer-price">$19</p>
      <span class="art art-mini-glasses" role="img" aria-label="Small illustrated sunglasses"></span>
      <span class="art art-flipflops" role="img" aria-label="Pair of yellow polka-dot flip flops with red straps"></span>
    </section>

    <svg class="art art-sunglasses" viewBox="0 0 422 390" role="img" aria-label="Photo of round sunglasses with teal mirrored lenses">
      <defs>
        <linearGradient id="lens-tone" x1="0" y1="0" x2="1" y2="1">
          <stop offset="0" stop-color="#0f3f4a"/>
          <stop offset="0.5" stop-color="#1fa6a6"/>
          <stop offset="1" stop-color="#3fcfc6"/>
        </linearGradient>
      </defs>
      <circle cx="320" cy="102" r="100" fill="url(#lens-tone)"/>
      <circle cx="106" cy="284" r="104" fill="url(#lens-tone)"/>
    </svg>

    <ul class="brand-row">
      <li class="brand-name">Kelo Vorn</li>
      <li class="brand-name">Varne</li>
      <li class="brand-name">Dex pold</li>
    </ul>
  </main>
</body>
</html>
```